Rural contractor needs professional informative business card

We need a business card design that looks professional but also includes information about the services that the business offers.
The business is an earthmoving and transport business. All of the services offered are listed on the old card attached.
The business is aimed at farmers so the design we are after is a classic look. The card needs to include all of the information that is listed on the old card design uploaded as an attachment. We recognize that this is a lot of information to fit on a business card but it also operates as a key marketing tool so is very important to the business.
Feel free to send me your questions.
Thanks
Reason: We are having trouble deciding between all these great designs - thank you for your efforts
We would love to see some designs using red with a little white and black. Also feel free to re-design our logo if you feel it needs to be to fit your designs. Thank you

```html
<!DOCTYPE html>
<html lang="en">
<head>
<meta charset="utf-8">
<title>RT Hallett Contracting – Business Card</title>
<link href="https://fonts.googleapis.com/css2?family=Montserrat:wght@500;600;700&display=swap" rel="stylesheet">
<style>
  :root {
    --bg: #3a3a3c;
    --card-black: #050505;
    --red: #e0242b;
    --white: #ffffff;
    --ink: #111111;
    --sky-top: #4a8fd8;
    --sky-low: #bcd6ee;
    --ground: #c9b59a;
    --dusk-top: #f3f1ef;
    --dusk-low: #e9c9c4;
    --field: #8b8066;
  }
  * { box-sizing: border-box; margin: 0; padding: 0; }
  html, body { width: 1200px; height: 800px; overflow: hidden; }
  body {
    background: var(--bg);
    font-family: "Montserrat", Arial, sans-serif;
    position: relative;
  }
  .card {
    position: absolute;
    top: 235px;
    width: 540px;
    height: 330px;
    background: var(--card-black);
    overflow: hidden;
    box-shadow: 0 14px 30px rgba(0,0,0,.45);
  }
  .card--services { left: 30px; }
  .card--contact { left: 630px; }

  /* services side */
  .services-photo {
    position: absolute; left: 0; top: 0; width: 100%; height: 160px;
    background: linear-gradient(180deg, var(--sky-top) 0%, var(--sky-low) 55%, var(--ground) 70%, #b9a283 100%);
  }
  .divider {
    position: absolute; left: 0; width: 100%; height: 3px; background: var(--red);
  }
  .card--services .divider { top: 160px; }
  .service-group { position: absolute; color: var(--white); }
  .service-group--earthmoving { left: 34px; top: 184px; }
  .service-group--transport { left: 330px; top: 236px; }
  .service-heading {
    color: var(--red); font-weight: 600; font-size: 12px;
    letter-spacing: 1.5px; text-transform: uppercase; margin-bottom: 5px;
  }
  .service-list { list-style: none; }
  .service-list li {
    display: flex; align-items: center; gap: 8px;
    font-size: 12.5px; font-weight: 600; letter-spacing: .6px; line-height: 17px;
  }
  .tick { width: 11px; height: 10px; flex: none; }

  /* contact side */
  .contact-photo {
    position: absolute; left: 0; top: 0; width: 100%; height: 200px;
    background: linear-gradient(180deg, var(--dusk-top) 0%, var(--dusk-top) 30%, var(--dusk-low) 55%, #a89d85 72%, var(--field) 100%);
  }
  .brand {
    position: absolute; left: 60px; top: 26px;
    display: flex; align-items: center; gap: 10px;
    color: var(--ink); font-weight: 700; font-size: 28px; letter-spacing: .5px;
  }
  .brand-square { width: 14px; height: 14px; background: var(--ink); }
  .tagline {
    position: absolute; left: 24px; top: 176px;
    color: var(--ink); font-weight: 700; font-size: 11.5px; letter-spacing: .6px;
  }
  .card--contact .divider { top: 200px; }
  .contact-name {
    position: absolute; left: 24px; top: 216px;
    color: var(--red); font-weight: 700; font-size: 23px; letter-spacing: 1.8px;
  }
  .contact-rule {
    position: absolute; left: 24px; top: 250px; width: 300px; height: 1px;
    background: rgba(255,255,255,.35);
  }
  .contact-details {
    position: absolute; left: 24px; top: 258px;
    color: var(--white); font-style: normal; font-size: 13px; font-weight: 500;
    letter-spacing: 1px; line-height: 20px;
  }
  .contact-details .label { color: var(--red); }
</style>
</head>
<body>
  <section class="card card--services" aria-label="Card back: services">
    <div class="services-photo" role="img" aria-label="Photo of a white prime mover towing empty flat-bed trailers under a clear blue sky"></div>
    <div class="divider"></div>

    <div class="service-group service-group--earthmoving">
      <h2 class="service-heading">Earthmoving</h2>
      <ul class="service-list">
        <li><svg class="tick" viewBox="0 0 11 10"><path d="M1 5.5 L4 8.5 L10 1.5" fill="none" stroke="#e0242b" stroke-width="2.2"/></svg>Road Building &amp; Maintenance</li>
        <li><svg class="tick" viewBox="0 0 11 10"><path d="M1 5.5 L4 8.5 L10 1.5" fill="none" stroke="#e0242b" stroke-width="2.2"/></svg>Poly Pipe Laying</li>
        <li><svg class="tick" viewBox="0 0 11 10"><path d="M1 5.5 L4 8.5 L10 1.5" fill="none" stroke="#e0242b" stroke-width="2.2"/></svg>Clearing Fence Lines</li>
        <li><svg class="tick" viewBox="0 0 11 10"><path d="M1 5.5 L4 8.5 L10 1.5" fill="none" stroke="#e0242b" stroke-width="2.2"/></svg>Sand &amp; Gravel Supplies</li>
      </ul>
    </div>

    <div class="service-group service-group--transport">
      <h2 class="service-heading">Transport</h2>
      <ul class="service-list">
        <li><svg class="tick" viewBox="0 0 11 10"><path d="M1 5.5 L4 8.5 L10 1.5" fill="none" stroke="#e0242b" stroke-width="2.2"/></svg>Grain</li>
        <li><svg class="tick" viewBox="0 0 11 10"><path d="M1 5.5 L4 8.5 L10 1.5" fill="none" stroke="#e0242b" stroke-width="2.2"/></svg>Cotton</li>
        <li><svg class="tick" viewBox="0 0 11 10"><path d="M1 5.5 L4 8.5 L10 1.5" fill="none" stroke="#e0242b" stroke-width="2.2"/></svg>Sand &amp; Gravel</li>
        <li><svg class="tick" viewBox="0 0 11 10"><path d="M1 5.5 L4 8.5 L10 1.5" fill="none" stroke="#e0242b" stroke-width="2.2"/></svg>Wool</li>
      </ul>
    </div>
  </section>

  <section class="card card--contact" aria-label="Card front: contact">
    <div class="contact-photo" role="img" aria-label="Photo of a white road train loaded with round cotton modules at dusk"></div>
    <div class="brand"><span class="brand-square"></span>RT Hallett Contracting</div>
    <p class="tagline">Earthmoving &amp; Transport Solutions</p>
    <div class="divider"></div>
    <h1 class="contact-name">Lachlan Hallett</h1>
    <div class="contact-rule"></div>
    <address class="contact-details">
      47 Dalby Street, Trangie 2823<br>
      <span class="label">P:</span> 0400 555 217 | <span class="label">E:</span> lhallett@ruralmail.com
    </address>
  </section>
</body>
</html>
```